Small Business Consulting Firm Needs Business Card Design

Need a sleek modern business card with 2 sides matching the colors of our logo. We will be placing these with a mailer we are sending out. These business cards will only ever be given to business owners. We operate helping businesses who are struggling with cash flow or finances. If the green and blue design needs to be moved to the right of "Brightpath Ledger Consulting" for aesthetic purposes that is ok. We will need an editable file if possible. We would like to include the reps name, email, website, and phone number. For now just use Owen Parrish, oparrish@brightpathledger.com, www.brightpathledger.com, and 855-219-7038.

```html
<!DOCTYPE html>
<html lang="en">
<head>
<meta charset="UTF-8">
<title>Brightpath Ledger Consulting – Business Card</title>
<link rel="stylesheet" href="https://fonts.googleapis.com/css2?family=Montserrat:wght@400;500;700&display=swap">
<style>
  :root {
    --backdrop: #dcdcda;
    --card-white: #fbfbfa;
    --card-dark: #2f2f31;
    --mark-dark: #232325;
    --ink: #3c3c3e;
    --ink-soft: #5a5a5c;
    --brand-blue: #1a6fc0;
    --brand-green: #5aa636;
    --edge-blue: #1577c9;
  }
  * { box-sizing: border-box; margin: 0; padding: 0; }
  html, body { width: 1200px; height: 801px; overflow: hidden; }
  body {
    background: var(--backdrop);
    font-family: "Montserrat", sans-serif;
    display: flex;
    align-items: center;
    justify-content: center;
    gap: 44px;
  }
  .card {
    width: 520px;
    height: 298px;
    position: relative;
    border-bottom: 4px solid var(--edge-blue);
    box-shadow: 0 6px 18px rgba(0,0,0,0.12);
  }
  .card--front {
    background: var(--card-white);
    display: flex;
    align-items: center;
  }
  .card--back {
    background: var(--card-dark);
    display: flex;
    align-items: center;
    justify-content: center;
  }
  .brand {
    width: 262px;
    display: flex;
    flex-direction: column;
    align-items: center;
    gap: 8px;
  }
  .brand__square {
    width: 22px;
    height: 22px;
    background: var(--brand-green);
    margin-bottom: 6px;
  }
  .brand__name {
    font-weight: 400;
    font-size: 19px;
    letter-spacing: 1.5px;
    color: var(--ink);
    text-transform: uppercase;
    text-align: center;
    line-height: 1.2;
  }
  .brand__tag {
    font-weight: 400;
    font-size: 9px;
    letter-spacing: 6px;
    color: var(--ink);
    text-transform: uppercase;
  }
  .divider {
    width: 1.5px;
    height: 118px;
    background: var(--brand-blue);
  }
  .rep {
    padding-left: 24px;
    display: flex;
    flex-direction: column;
  }
  .rep__name {
    font-weight: 700;
    font-size: 18px;
    color: var(--brand-blue);
    text-transform: uppercase;
    letter-spacing: 0.5px;
  }
  .rep__title {
    font-size: 12px;
    color: var(--ink-soft);
    margin-bottom: 14px;
  }
  .contact {
    list-style: none;
    display: flex;
    flex-direction: column;
    gap: 3px;
  }
  .contact__item {
    display: flex;
    align-items: center;
    gap: 6px;
    font-size: 11.5px;
    color: var(--ink);
  }
  .contact__icon { width: 10px; height: 10px; flex: none; }
  .back-brand {
    display: flex;
    flex-direction: column;
    align-items: center;
    gap: 10px;
    color: var(--mark-dark);
  }
  .back-brand .brand__square { background: var(--mark-dark); width: 30px; height: 30px; }
  .back-brand .brand__name { color: var(--mark-dark); font-size: 24px; letter-spacing: 2.5px; }
  .back-brand .brand__tag { color: var(--mark-dark); font-size: 10px; letter-spacing: 8px; }
</style>
</head>
<body>
  <section class="card card--front" aria-label="Card front">
    <div class="brand">
      <div class="brand__square"></div>
      <p class="brand__name">Brightpath Ledger</p>
      <p class="brand__tag">Consulting</p>
    </div>
    <div class="divider"></div>
    <div class="rep">
      <h1 class="rep__name">Owen Parrish</h1>
      <p class="rep__title">President</p>
      <ul class="contact">
        <li class="contact__item">
          <svg class="contact__icon" viewBox="0 0 10 10"><path d="M2 0.5 L3.6 2.6 L2.8 3.6 Q4 6 6.4 7.2 L7.4 6.4 L9.5 8 L8.4 9.5 Q3.8 9 0.5 1.6 Z" fill="var(--brand-green)"/></svg>
          855-219-7038
        </li>
        <li class="contact__item">
          <svg class="contact__icon" viewBox="0 0 10 10"><rect x="0.5" y="2" width="9" height="6.5" fill="var(--brand-green)"/><path d="M0.5 2 L5 5.6 L9.5 2" fill="none" stroke="#fff" stroke-width="0.9"/></svg>
          oparrish@brightpathledger.com
        </li>
        <li class="contact__item">
          <svg class="contact__icon" viewBox="0 0 10 10"><circle cx="5" cy="5" r="4.5" fill="var(--brand-green)"/><path d="M0.5 5 H9.5 M5 0.5 V9.5 M1.5 2.8 H8.5 M1.5 7.2 H8.5" stroke="#fff" stroke-width="0.6"/></svg>
          www.brightpathledger.com
        </li>
      </ul>
    </div>
  </section>

  <section class="card card--back" aria-label="Card back">
    <div class="back-brand">
      <div class="brand__square"></div>
      <p class="brand__name">Brightpath Ledger</p>
      <p class="brand__tag">Consulting</p>
    </div>
  </section>
</body>
</html>
```